Refresh web site from year 2003

Voltaro Forma has a web site (https://vfprosjekt.no/) from early 2000 that needs to be refreshed.

Attached are company logo, favicon files, a licensed image to be used, an animation that illustrate the use of one of the products.

Target Market(s)

Industrial customers

Industry/Entity Type

Electrical Switch Board Builders, Automation Industry

Coding

Coded - Design and coding required

Number of Pages Required

3 page

Requirements
Must have
• WordPress site. Use attached animation in the front page (source file is in Adobe Animation format, if adjustments are needed). Product page for two products, "QRT" and "KV-7 Typ B".
Nice to have
• The site should focus on promoting two products QRT and KV-7 Typ B.

```html
<!DOCTYPE html>
<html lang="en">
<head>
<meta charset="utf-8">
<title>Voltaro Forma</title>
<link href="https://fonts.googleapis.com/css2?family=Lato:wght@400;700;900&display=swap" rel="stylesheet">
<style>
:root{
  --blue:#0b4a8f;
  --blue-card:#0a3f7c;
  --ink:#2a2f36;
  --text:#555b63;
  --line:#e3e6ea;
  --footer:#1b1c1e;
  --white:#ffffff;
}
*{margin:0;padding:0;box-sizing:border-box}
html,body{width:1200px;height:3720px;overflow:hidden}
body{font-family:'Lato',sans-serif;color:var(--text);background:var(--white);position:relative}
.abs{position:absolute}
a{color:inherit;text-decoration:none}

/* header */
.site-header{left:0;top:0;width:1200px;height:118px;background:var(--white)}
.brand{left:111px;top:18px;font-size:36px;font-weight:900;color:var(--blue);line-height:40px;width:220px}
.topbar{left:655px;top:19px;font-size:18px;color:var(--ink);display:flex;gap:12px;align-items:center}
.topbar svg{width:15px;height:15px;fill:var(--blue);vertical-align:-2px;margin-right:3px}
.flags{left:1035px;top:24px;display:flex;gap:8px}
.flags span{width:22px;height:14px;display:block;border-radius:1px}
.nav{left:631px;top:64px;display:flex;gap:29px;font-size:19px;color:var(--ink)}
.nav .active{color:var(--blue)}

/* hero */
.hero{left:0;top:118px;width:1200px;height:637px;background:linear-gradient(90deg,#bfc3c6 0%,#a9adb0 35%,#8c9296 60%,#b6b9b5 100%)}
.hero-title{left:111px;top:232px;font-size:62px;font-weight:700;color:var(--white);line-height:68px}
.hero-sub{left:111px;top:386px;width:370px;font-size:20px;line-height:33px;color:var(--white)}
.btn{display:flex;align-items:center;justify-content:center;background:var(--blue);color:var(--white);font-weight:700;border-radius:40px;letter-spacing:.3px}
.hero-btn{left:111px;top:515px;width:207px;height:63px;font-size:18px}

/* about */
.about-band{left:0;top:755px;width:1200px;height:715px;background:#fbfcfd}
.about-photo{left:110px;top:869px;width:462px;height:462px;border-radius:50%;background:radial-gradient(circle at 40% 40%,#6b8bb0,#3a4f66 55%,#c9b8a8 100%)}
.ring{border-radius:50%;border:2px solid #d4dfeb}
.kicker{font-size:20px;color:var(--ink);font-weight:700}
.heading{font-weight:900;color:var(--ink)}
.about-copy{left:679px;top:966px;width:450px}
.about-copy p{font-size:16.5px;line-height:27.5px;color:var(--text)}

/* services */
.services{left:0;top:1470px;width:1200px;height:624px;background:linear-gradient(120deg,#0b4f9c 0%,#0a4a92 60%,#084285 100%)}
.card{width:309px;height:295px;padding:0 30px}
.card h3{font-size:22px;font-weight:700;margin-top:8px}
.card p{font-size:16.5px;line-height:26px;margin-top:10px}
.card.dark{background:var(--blue-card);color:var(--white)}
.card.light{background:var(--white);color:var(--ink)}
.card.light p{color:var(--text)}
.card svg{width:104px;height:104px;margin-top:26px;margin-left:-2px}

/* products */
.tabs{left:111px;top:2290px;width:977px;height:73px;border-bottom:3px solid var(--line)}
.tab{top:0;font-size:18.5px;line-height:27px;color:var(--ink)}
.tab-active{left:36px;top:67px;width:100px;height:4px;background:var(--blue)}
.product-photo{background:linear-gradient(135deg,#f7f7f7,#ececec);box-shadow:0 4px 18px rgba(0,0,0,.12)}
.product-title{font-size:28px;font-weight:700;color:var(--ink);line-height:36px}
.bullets{list-style:none;font-size:16.5px;color:var(--text)}
.bullets li{height:33.5px;display:flex;align-items:center;gap:12px}
.bullets svg{width:15px;height:15px}
.small-btn{height:54px;width:159px;font-size:18px}

/* footer */
.site-footer{left:0;top:3322px;width:1200px;height:398px;background:var(--footer)}
.on-dark{color:var(--white)}
.foot-brand{left:111px;top:3440px;font-size:40px;font-weight:900;line-height:46px;width:220px}
.foot-h{font-size:19px;font-weight:700}
.foot-list{font-size:16.5px;line-height:32.5px;list-style:none}
.contact-row{font-size:16.5px;display:flex;gap:12px;align-items:flex-start;line-height:19px}
.contact-row svg{width:14px;height:14px;fill:var(--white);flex:none;margin-top:2px}
.social{left:896px;top:3416px;display:flex;gap:9px}
.social span{width:38px;height:38px;border:1.5px solid var(--white);border-radius:50%}
.foot-rule{left:111px;top:3635px;width:977px;height:1px;background:#3a3c40}
.copy{left:0;top:3660px;width:1200px;text-align:center;font-size:16.5px}
</style>
</head>
<body>

<header class="abs site-header">
  <div class="abs brand">Voltaro<br>Forma</div>
  <div class="abs topbar">
    <span><svg viewBox="0 0 16 16"><path d="M3 1l3 3-2 2c1 2 3 4 6 6l2-2 3 3-2 2C7 15 1 9 1 3z"/></svg>+47 900 14 287</span>
    <span>|</span>
    <span><svg viewBox="0 0 16 16"><path d="M1 3h14v10H1z"/></svg>post@voltaroforma.no</span>
  </div>
  <div class="abs flags"><span style="background:#c8202f"></span><span style="background:#1f3f86"></span></div>
  <nav class="abs nav">
    <a class="active">Home</a><a>About us</a><a>Services</a><a>Products</a><a>Contact</a>
  </nav>
</header>

<section class="abs hero" role="img" aria-label="Photograph of industrial electrical switchboard cabinets with indicator lamps"></section>
<h1 class="abs hero-title">Voltaro<br>Forma</h1>
<p class="abs hero-sub">Production &amp; development company for electronics with emphasis on small series production.</p>
<a class="abs btn hero-btn">GET MORE INFO</a>

<section class="abs about-band"></section>
<div class="abs ring" style="left:55px;top:814px;width:572px;height:572px"></div>
<div class="abs ring" style="left:80px;top:839px;width:522px;height:522px;border-color:#e3eaf2"></div>
<div class="abs about-photo" role="img" aria-label="Photograph of a hand wiring coloured jumper cables on a breadboard"></div>
<svg class="abs" style="left:676px;top:862px" width="72" height="62" viewBox="0 0 72 62"><path d="M28 12H4v38h36" fill="none" stroke="#0b4a8f" stroke-width="3"/><circle cx="28" cy="12" r="7" fill="#0b4a8f"/><circle cx="62" cy="54" r="7" fill="#0b4a8f"/></svg>
<div class="abs kicker" style="left:722px;top:860px">Welcome to</div>
<h2 class="abs heading" style="left:754px;top:890px;font-size:37px">Voltaro Forma</h2>
<div class="abs about-copy">
  <p>Voltaro Forma is a production and development company for electronics with emphasis on small series production.</p>
  <p style="margin-top:27px">We are today two employees with good and relevant access to additional expertise in the established network. The company was established in 1985 and has since 2001 taken over production equipment and production basis from another company in the same industry.</p>
</div>
<a class="abs btn" style="left:679px;top:1256px;width:159px;height:55px;font-size:18px">READ MORE</a>

<section class="abs services"></section>
<svg class="abs" style="left:111px;top:1528px" width="72" height="62" viewBox="0 0 72 62"><path d="M28 12H4v38h36" fill="none" stroke="#fff" stroke-width="3"/><circle cx="28" cy="12" r="7" fill="#fff"/><circle cx="62" cy="54" r="7" fill="#fff"/></svg>
<div class="abs kicker" style="left:156px;top:1525px;color:#fff">Our</div>
<h2 class="abs heading" style="left:187px;top:1556px;font-size:35px;color:#fff">Services</h2>
<p class="abs" style="left:111px;top:1628px;width:800px;font-size:16.5px;line-height:27.5px;color:#fff">Our mission is to contribute good and cost effective electronics products for the industrial market, as well as seek and develop solutions to new and existing concepts.</p>

<div class="abs card dark" style="left:111px;top:1724px">
  <svg viewBox="0 0 100 100" fill="none" stroke="#fff" stroke-width="3"><circle cx="50" cy="50" r="38"/><circle cx="50" cy="50" r="28"/><rect x="38" y="38" width="24" height="24"/><rect x="44" y="44" width="12" height="12"/><path d="M50 4v8M50 88v8M4 50h8M88 50h8M18 18l6 6M76 76l6 6M18 82l6-6M76 24l6-6"/></svg>
  <h3>Production</h3>
  <p>Small series production of electronic units in the number of 10 to 200 units.</p>
</div>
<div class="abs card light" style="left:446px;top:1724px">
  <svg viewBox="0 0 100 100" fill="none" stroke="#0b4a8f" stroke-width="3"><path d="M52 10a38 38 0 1 0 0 80"/><path d="M52 24a24 24 0 1 0 0 52"/><path d="M52 40h20M52 50h34M52 60h20M72 40l8-12M72 60l8 12"/><circle cx="82" cy="26" r="4"/><circle cx="90" cy="50" r="4"/><circle cx="82" cy="74" r="4"/></svg>
  <h3>Devolepment</h3>
  <p>Development of product concept to finished product in collaboration with a customer.</p>
</div>
<div class="abs card dark" style="left:780px;top:1724px">
  <svg viewBox="0 0 100 100" fill="none" stroke="#fff" stroke-width="3"><path d="M8 10h84"/><rect x="44" y="5" width="12" height="10"/><path d="M22 90a40 40 0 0 1 22-72M78 90a40 40 0 0 0-22-72"/><path d="M50 20l-14 36 10 12v28h8V68l10-12z"/><circle cx="50" cy="50" r="4"/></svg>
  <h3>Design</h3>
  <p>Designing of electronics and print cards for pre-assembled and tested unit.</p>
</div>

<svg class="abs" style="left:491px;top:2166px" width="72" height="62" viewBox="0 0 72 62"><path d="M28 12H4v38h36" fill="none" stroke="#0b4a8f" stroke-width="3"/><circle cx="28" cy="12" r="7" fill="#0b4a8f"/><circle cx="62" cy="54" r="7" fill="#0b4a8f"/></svg>
<div class="abs kicker" style="left:535px;top:2163px">Our</div>
<h2 class="abs heading" style="left:567px;top:2194px;font-size:35px">Products</h2>

<div class="abs tabs">
  <div class="abs tab" style="left:50px">LED<br>products</div>
  <div class="abs tab" style="left:173px">Galvanic<br>isolation modules</div>
  <div class="abs tab" style="left:368px">Panel<br>Instruments</div>
  <div class="abs tab" style="left:521px">Measurement<br>value converters</div>
  <div class="abs tab" style="left:711px">Under<br>Voltage Relay</div>
  <div class="abs tab" style="left:875px">Flame<br>Guard</div>
  <div class="abs tab-active"></div>
</div>

<div class="abs product-photo" style="left:111px;top:2426px;width:491px;height:358px" role="img" aria-label="Product photo of signal lamps, an emergency stop button and a rotary selector"></div>
<h3 class="abs product-title" style="left:703px;top:2455px;width:360px">Signal Lamp with built-in LED Type VL</h3>
<ul class="abs bullets" style="left:707px;top:2547px">
  <li><svg viewBox="0 0 16 16"><circle cx="8" cy="8" r="8" fill="#0b4a8f"/><path d="M4.5 8.3l2.3 2.2 4.7-4.8" stroke="#fff" stroke-width="1.8" fill="none"/></svg>Very long operating time</li>
  <li><svg viewBox="0 0 16 16"><circle cx="8" cy="8" r="8" fill="#0b4a8f"/><path d="M4.5 8.3l2.3 2.2 4.7-4.8" stroke="#fff" stroke-width="1.8" fill="none"/></svg>Easy mounting</li>
  <li><svg viewBox="0 0 16 16"><circle cx="8" cy="8" r="8" fill="#0b4a8f"/><path d="M4.5 8.3l2.3 2.2 4.7-4.8" stroke="#fff" stroke-width="1.8" fill="none"/></svg>Reliable reading at long distance</li>
  <li><svg viewBox="0 0 16 16"><circle cx="8" cy="8" r="8" fill="#0b4a8f"/><path d="M4.5 8.3l2.3 2.2 4.7-4.8" stroke="#fff" stroke-width="1.8" fill="none"/></svg>Wide angle</li>
</ul>
<a class="abs btn small-btn" style="left:709px;top:2705px">READ MORE</a>

<h3 class="abs product-title" style="left:111px;top:2897px;width:420px">Electrical Light Switch Indicator Type QRT</h3>
<ul class="abs bullets" style="left:115px;top:2980px">
  <li><svg viewBox="0 0 16 16"><circle cx="8" cy="8" r="8" fill="#0b4a8f"/><path d="M4.5 8.3l2.3 2.2 4.7-4.8" stroke="#fff" stroke-width="1.8" fill="none"/></svg>Very long operating time due to the LED</li>
  <li><svg viewBox="0 0 16 16"><circle cx="8" cy="8" r="8" fill="#0b4a8f"/><path d="M4.5 8.3l2.3 2.2 4.7-4.8" stroke="#fff" stroke-width="1.8" fill="none"/></svg>Easy mounting</li>
  <li><svg viewBox="0 0 16 16"><circle cx="8" cy="8" r="8" fill="#0b4a8f"/><path d="M4.5 8.3l2.3 2.2 4.7-4.8" stroke="#fff" stroke-width="1.8" fill="none"/></svg>Reliable reading at long distance</li>
  <li><svg viewBox="0 0 16 16"><circle cx="8" cy="8" r="8" fill="#0b4a8f"/><path d="M4.5 8.3l2.3 2.2 4.7-4.8" stroke="#fff" stroke-width="1.8" fill="none"/></svg>Wide angle</li>
</ul>
<a class="abs btn small-btn" style="left:116px;top:3138px">READ MORE</a>

<div class="abs product-photo" style="left:592px;top:2865px;width:491px;height:358px" role="img" aria-label="Animation showing the indicator mounted in a switchboard and wired in its circuit"></div>

<footer class="abs site-footer"></footer>
<div class="abs foot-brand on-dark">Voltaro<br>Forma</div>
<div class="abs foot-h on-dark" style="left:413px;top:3370px">Quick Links</div>
<ul class="abs foot-list on-dark" style="left:414px;top:3412px">
  <li>Home</li><li>About us</li><li>Services</li><li>Products</li><li>Contact</li>
</ul>
<div class="abs foot-h on-dark" style="left:621px;top:3370px">Contact Us</div>
<div class="abs on-dark" style="left:621px;top:3419px;display:flex;flex-direction:column;gap:20px">
  <div class="contact-row"><svg viewBox="0 0 16 16"><path d="M8 0a5 5 0 0 1 5 5c0 4-5 11-5 11S3 9 3 5a5 5 0 0 1 5-5zm0 3a2 2 0 1 0 0 4 2 2 0 0 0 0-4z"/></svg><span>Lindalsvegen 48<br>N-4720 Heimdal<br>Norway</span></div>
  <div class="contact-row"><svg viewBox="0 0 16 16"><path d="M3 1l3 3-2 2c1 2 3 4 6 6l2-2 3 3-2 2C7 15 1 9 1 3z"/></svg><span>+47 900 14 287</span></div>
  <div class="contact-row"><svg viewBox="0 0 16 16"><path d="M1 3h14v10H1z"/></svg><span>post@voltaroforma.no</span></div>
  <div class="contact-row"><svg viewBox="0 0 16 16"><circle cx="8" cy="8" r="7"/></svg><span>www.vfprosjekt.no</span></div>
</div>
<div class="abs foot-h on-dark" style="left:896px;top:3370px">Social Media</div>
<div class="abs social"><span></span><span></span><span></span></div>
<div class="abs foot-rule"></div>
<div class="abs copy on-dark">Copyright © 2003-2021 Voltaro Forma.</div>

</body>
</html>
```